Website for new dental office

I am Dr. Colin Marsh and am building a new dental practice. I specialize in general dentistry. I am young and have a higher end dental practice incorporating very new technologies and would like my website to reflect that. As many dental patients are older, the website must be very easy to navigate. I would like patients to be able to request appointments, and will eventually add on patient information forms (the health history, etc, that you normally fill out in the practice) from my practice management software, so leave an area for that.

Industry/Entity Type

Building

```html
<!DOCTYPE html>
<html lang="en">
<head>
<meta charset="utf-8">
<title>Marsh Dental Clinic</title>
<link href="https://fonts.googleapis.com/css2?family=Oswald:wght@300;400&family=Roboto:ital,wght@0,300;0,400;0,500;1,300;1,400&display=swap" rel="stylesheet">
<style>
:root{
  --sky:#21b9f5;
  --orange:#ff8a00;
  --green-dark:#4a8f06;
  --ink:#3c3c3c;
  --text:#555;
  --line:#e2e2e2;
  --footer:#444;
  --footer-base:#333;
  --footer-text:#d6d6d6;
  --card-dark:#2e2e2e;
  --white:#fff;
}
*{box-sizing:border-box;margin:0;padding:0}
html,body{width:1170px;height:1200px;overflow:hidden;background:#fff}
body{font-family:'Roboto',sans-serif;color:var(--text)}
.page{position:relative;width:1170px;height:1200px;overflow:hidden}
.abs{position:absolute}

.header-band{left:0;top:0;width:1170px;height:144px;background:var(--sky);border-top:5px solid var(--orange)}
.brand{left:72px;top:38px;display:flex;align-items:center;gap:10px;font-family:'Roboto',sans-serif;font-weight:500;font-size:24px;color:var(--white);line-height:1;white-space:nowrap}
.brand-dot{width:14px;height:14px;border-radius:50%;background:var(--white)}
.call-tab{left:905px;top:4px;width:193px;height:29px;background:var(--orange);border-radius:0 0 7px 7px;color:var(--white);font-size:17px;text-align:center;line-height:27px}
.main-nav{left:378px;top:64px;display:flex}
.main-nav a{font-size:13px;color:#253342;text-decoration:none;letter-spacing:.2px;margin-right:27.5px}
.main-nav a.current{color:var(--white)}

.hero-frame{left:72px;top:95px;width:1026px;height:375px;background:#fff;box-shadow:0 1px 4px rgba(0,0,0,.25)}
.hero-photo{left:76.5px;top:100px;width:1017px;height:365px;background:linear-gradient(100deg,#d9d6cc 0%,#c9c4b5 30%,#9bb6cc 55%,#d8d4c6 80%,#c9c5b6 100%)}
.dots{left:94px;top:430px;display:flex;gap:5px}
.dots span{width:14px;height:14px;border-radius:50%;background:#111}
.dots span.on{background:var(--sky)}
.appt{left:774px;top:121px;width:300px;height:323px;background:#f3f3f1;border:1px solid #ddd;box-shadow:0 1px 3px rgba(0,0,0,.15);padding:0 17px}
.appt h2{font-family:'Oswald',sans-serif;font-weight:400;font-size:24px;color:var(--ink);margin:17px 0 12px;letter-spacing:-.2px}
.field{height:32px;background:#fff;border:1px solid #dcdcdc;font-size:12px;color:#888;padding:9px 11px;margin-bottom:6px}
.field.tall{height:87px}
.appt-btn{margin-top:13px;height:40px;background:linear-gradient(#66b515,var(--green-dark));color:#fff;font-size:16px;text-align:center;line-height:40px;letter-spacing:.3px}

.card{top:483px;width:322px;height:136px;border:1px solid #ddd;background:#fff;padding:3px}
.card-in{position:relative;width:100%;height:100%;background:linear-gradient(90deg,var(--photo) 0%,var(--photo) 40%,#444 62%,var(--card-dark) 100%)}
.card h3{position:absolute;left:182px;font-family:'Oswald',sans-serif;font-weight:400;color:#fff;font-size:28px;line-height:30px}
.card a{position:absolute;left:182px;top:99px;color:var(--sky);font-size:11.5px;text-decoration:none;letter-spacing:.3px}

.section-title{font-family:'Oswald',sans-serif;font-weight:300;color:var(--sky);font-size:25px}
.welcome{left:72px;top:646px;width:590px}
.welcome p{font-size:12px;line-height:20.7px;margin-top:12px;margin-bottom:-5px}
.welcome p+p{margin-top:12px}
.read-more{left:72px;top:872px;width:103px;height:31px;background:var(--sky);color:#fff;font-size:13px;text-align:center;line-height:31px;border-radius:2px}
.divider{left:686px;top:652px;width:1px;height:249px;background:var(--line)}
.testi-title{left:712px;top:646px}
.quote{left:711px;top:696px;width:386px;height:113px;background:#f4f4f4;box-shadow:0 1px 2px rgba(0,0,0,.08);padding:14px 16px 0 18px;font-size:11.5px;font-style:italic;font-weight:300;line-height:20.7px;color:#444}
.quote-mark{left:723px;top:700px;font-family:Georgia,serif;font-size:48px;color:#ccc;line-height:1}
.tail{left:805px;top:808px}
.avatar{left:711px;top:834px;width:67px;height:68px;border:1px solid #ddd;padding:3px;background:#fff}
.avatar div{width:100%;height:100%;background:linear-gradient(#d8c6a6,#e6cfa9)}
.person{left:792px;top:869px;font-size:12px;color:#333}
.person em{display:block;color:var(--orange);font-size:12px;margin-top:2px}

.footer{left:0;top:931px;width:1170px;height:207px;background:var(--footer)}
.fcol{top:954px;width:200px}
.fcol h4{font-weight:400;font-size:17px;color:var(--sky);margin-bottom:8px}
.fcol li{list-style:none;font-size:11.5px;color:var(--footer-text);line-height:25.2px;font-weight:300}
.contact p{font-size:11.5px;color:var(--footer-text);line-height:18px;font-weight:300}
.contact .row{display:flex;line-height:20px;font-size:11.5px;color:var(--footer-text);font-weight:300}
.contact .row span:first-child{width:65px}
.contact .row span+span{color:var(--sky)}
.map{left:730px;top:958px;width:368px;height:164px;border:2px solid #999;background:linear-gradient(135deg,#e9e4d8,#dcdccc 50%,#e7e1d2)}
.base{left:0;top:1138px;width:1170px;height:62px;background:var(--footer-base)}
.copy{left:72px;top:1164px;font-size:11.5px;color:#bbb;font-weight:300}
.copy span{color:var(--sky)}
.social{left:930px;top:1155px;display:flex;gap:8px}
.social span{width:29px;height:29px;border-radius:50%;background:#6a6a6a}
</style>
</head>
<body>
<div class="page">

  <div class="abs header-band"></div>
  <div class="abs brand"><span class="brand-dot"></span>Marsh Dental Clinic</div>
  <div class="abs call-tab">CALL: 200 555 0148</div>
  <nav class="abs main-nav">
    <a class="current" href="#">HOME</a><a href="#">ABOUT</a><a href="#">SERVICES</a><a href="#">TEAM</a><a href="#">PORTFOLIO</a><a href="#">OUR OFFICE</a><a href="#">PATIENT RESOURCES</a><a href="#" style="margin-right:0">CONTACT US</a>
  </nav>

  <div class="abs hero-frame"></div>
  <div class="abs hero-photo" role="img" aria-label="Photo of a smiling dentist with a patient in the treatment chair"></div>
  <div class="abs dots"><span class="on"></span><span></span><span></span><span></span></div>
  <form class="abs appt">
    <h2>REQUEST AN APPOINTMENT</h2>
    <div class="field">Full Name</div>
    <div class="field">Phone Number</div>
    <div class="field">Email Address</div>
    <div class="field tall">Comments</div>
    <div class="appt-btn">REQUEST AN APPOINTMENT</div>
  </form>

  <div class="abs card" style="left:72px">
    <div class="card-in" role="img" aria-label="Photo of a dentist treating a patient" style="--photo:#2f4f8a">
      <h3 style="top:25px">Our<br>Procedures</h3><a href="#">LEARN MORE</a>
    </div>
  </div>
  <div class="abs card" style="left:423px">
    <div class="card-in" role="img" aria-label="Photo of the clinic team in scrubs" style="--photo:#4a93c9">
      <h3 style="top:55px">Our Team</h3><a href="#">LEARN MORE</a>
    </div>
  </div>
  <div class="abs card" style="left:776px">
    <div class="card-in" role="img" aria-label="Street map with a location pin" style="--photo:#e6e4e0">
      <h3 style="top:25px">Our<br>Location</h3><a href="#">LEARN MORE</a>
    </div>
  </div>

  <section class="abs welcome">
    <h2 class="section-title">Welcome to Marsh Dental Clinic</h2>
    <p>Aliquam molestie, mi et imperdiet euismod, dui purus auctor tellus, et interdum lacus lectus et ante. Sed accumsan sollicitudin sapien, sit amet adipiscing turpis gravida ac. In congue, neque ac lobortis volutpat, libero mauris varius mi, vitae suscipit ipsum ligula vitae risus. Duis aliquam nibh a dui iaculis viverra id a velit. Vivamus egestas risus in magna varius commodo. Sed semper viverra egestas. Etiam pretium porttitor lectus, vel ornare neque porta volutpat.</p>
    <p>Aenean a nibh eget turpis vehicula tempus ac sed massa. Vestibulum dolor nulla, ultrices ac tincidunt sed, laoreet non est. Suspendisse lobortis turpis in odio blandit ac interdum lorem euismod. Etiam risus massa, vulputate eu pellentesque et, consectetur a neque.</p>
  </section>
  <div class="abs read-more">Read More</div>

  <div class="abs divider"></div>
  <h2 class="abs section-title testi-title">Testimonials</h2>
  <div class="abs quote">&emsp;&emsp;&ensp;Suspendisse lobortis turpis in odio blandit ac interdum lorem euismod. Etiam risus massa, vulputate eu pellentesque et, consectetur a neque. Etiam pretium porttitor lectus, vel ornare neque porta volutpat...</div>
  <div class="abs quote-mark">&ldquo;</div>
  <svg class="abs tail" width="46" height="22" viewBox="0 0 46 22"><path d="M0 0 L46 0 L0 22 Z" fill="#f4f4f4"/></svg>
  <div class="abs avatar"><div role="img" aria-label="Portrait photo of the reviewer"></div></div>
  <div class="abs person">Name Goes Here<em>Location</em></div>

  <footer class="abs footer"></footer>
  <div class="abs fcol" style="left:73px">
    <h4>Quick Links</h4>
    <ul><li>Lorem ipsum dolor</li><li>Sit amet consectetur</li><li>Adipisicing eitseo</li><li>Eiusmod tempor incididunt</li><li>Labore et dolore magna</li></ul>
  </div>
  <div class="abs fcol" style="left:284px">
    <h4>Services</h4>
    <ul><li>Lorem ipsum dolor</li><li>Sit amet consectetur</li><li>Adipisicing eitseo</li><li>Eiusmod tempor incididunt</li><li>Labore et dolore magna</li></ul>
  </div>
  <div class="abs fcol contact" style="left:497px;width:220px">
    <h4>Contact Info</h4>
    <p>Company Name Inc. 412 Harrow Lane,<br>Glasgow, G12 8QT.</p>
    <div class="row" style="margin-top:5px"><span>Freephone:</span><span>200 555 0148</span></div>
    <div class="row"><span>Fax:</span><span>200 555 0149</span></div>
    <div class="row"><span>Email:</span><span>info@marshdentalclinic.com</span></div>
  </div>
  <div class="abs map" role="img" aria-label="City street map showing the clinic location"></div>

  <div class="abs base"></div>
  <div class="abs copy">Copyright © 2014. <span>Marsh Dental Clinic</span>. All Right Reserved</div>
  <div class="abs social" aria-label="Social media links"><span></span><span></span><span></span><span></span><span></span></div>

</div>
</body>
</html>
```